velvet stride

Velvet Stride is a fitness studio that offers personal training and group classes. We are an upscale studio, more classy then hard core! Geared toward a more mature audience, 35-65. Please put place holders for any pictures needed, I have a ton of pics but need to see what is needed and where it'll go for placement! I attached a sample of a poster I made that I like just so you can get an idea. It doesn't need to look like this, it's just an idea!

Industry/Entity Type

Fitness

```html
<!DOCTYPE html>
<html lang="en">
<head>
<meta charset="utf-8">
<title>Velvet Stride – Trifold Brochure</title>
<link rel="stylesheet" href="https://fonts.googleapis.com/css2?family=Roboto:wght@300;400;500;700&family=Roboto+Condensed:wght@300;400;700&display=swap">
<style>
  :root{
    --page-bg:#e4e4e6;
    --charcoal:#3a3a3c;
    --charcoal-deep:#323234;
    --rose:#d14a55;
    --steel:#b3b3b7;
    --paper:#ffffff;
    --ink-light:#e2e2e2;
    --ink-muted:#c9c9cc;
  }
  *{margin:0;padding:0;box-sizing:border-box}
  html,body{width:811px;height:1200px;overflow:hidden;background:var(--page-bg)}
  body{position:relative;font-family:"Roboto",Arial,sans-serif}
  .brochure{
    position:absolute;left:20px;top:328px;width:914px;height:645px;
    transform:scale(0.8435);transform-origin:0 0;
    box-shadow:0 14px 28px rgba(0,0,0,.22);background:var(--paper);
  }
  .panel{position:absolute;top:0;height:645px;overflow:hidden}
  .panel--about{left:0;width:305px}
  .panel--contact{left:305px;width:305px;border-left:1px solid #d8d8d8}
  .panel--cover{left:610px;width:304px;border-left:1px solid #555}
  .panel-art{position:absolute;inset:0;width:100%;height:100%}

  /* About panel */
  .about-title{position:absolute;left:28px;top:12px;font-family:"Roboto Condensed",sans-serif;font-weight:700;font-size:22px;color:#fff}
  .about-title-rule{position:absolute;left:150px;top:22px;width:24px;height:18px;border-top:1.5px solid #fff;border-right:1.5px solid #fff}
  .about-copy{position:absolute;left:28px;top:50px;width:246px;color:var(--ink-light);font-size:10.6px;line-height:14.6px;text-align:justify}
  .about-copy p{margin-bottom:14px}

  /* Brand lockups */
  .brand{position:absolute;text-align:center;color:#fff;font-family:"Roboto",sans-serif;font-weight:300}
  .brand-dot{display:block;margin:0 auto 8px;border-radius:50%;background:#fff}
  .brand-name{display:block;text-transform:uppercase;white-space:nowrap}
  .brand-place{display:block;font-size:7px;letter-spacing:1.5px;text-transform:uppercase;color:var(--ink-muted);margin-top:6px}

  .brand--contact{left:153px;top:384px;width:160px}
  .brand--contact .brand-dot{width:18px;height:18px}
  .brand--contact .brand-name{font-size:12.5px;letter-spacing:2.5px}

  .social-row{position:absolute;left:172px;top:467px;display:flex;gap:4px}
  .social-row span{width:14px;height:14px;border-radius:50%;border:1.3px solid #fff}

  .contact-title{position:absolute;left:25px;top:492px;font-size:16px;color:#fff;font-weight:400;border-bottom:1px solid #fff;padding-bottom:1px}
  .contact-list{position:absolute;left:22px;top:523px;list-style:none;color:#fff}
  .contact-list li{display:flex;align-items:flex-start;gap:8px;margin-bottom:5px;font-size:13px;line-height:18px}
  .contact-list svg{flex:none;margin-top:3px}
  .contact-phone{font-size:16.5px;font-weight:700}
  .contact-mail{font-size:12px}
  .contact-web{font-size:14px}
  .contact-web b{font-weight:700}

  /* Cover panel */
  .brand--cover{left:0;top:372px;width:276px}
  .brand--cover .brand-dot{width:30px;height:30px;margin-bottom:16px}
  .brand--cover .brand-name{font-size:20px;letter-spacing:3.5px}
  .brand--cover .brand-place{font-size:10px;margin-top:10px;color:#fff}

  .cover-headline{position:absolute;left:11px;top:500px;width:265px;color:#fff;font-family:"Roboto Condensed",sans-serif;text-transform:uppercase;white-space:nowrap}
  .cover-kicker{display:block;font-size:25px;font-weight:700;line-height:28px}
  .cover-title{display:block;font-size:45px;font-weight:700;line-height:44px;letter-spacing:-1px;transform:scaleX(.88);transform-origin:left}
  .cover-method{display:block;font-family:"Roboto",sans-serif;font-weight:400;font-size:23px;letter-spacing:2.5px;line-height:26px;margin-top:4px}
  .cover-author{display:block;font-family:"Roboto",sans-serif;font-weight:400;font-size:20px;letter-spacing:1px;line-height:24px}

  .cover-spine{position:absolute;left:276px;top:468px;width:28px;height:177px;background:var(--paper)}
  .cover-spine span{position:absolute;left:50%;top:50%;transform:translate(-50%,-50%) rotate(-90deg);white-space:nowrap;font-size:13px;color:#333}
  .cover-spine b{color:var(--rose);font-weight:500}
</style>
</head>
<body>
<main class="brochure">

  <section class="panel panel--about">
    <svg class="panel-art" viewBox="0 0 305 645" aria-hidden="true">
      <polygon points="0,0 305,0 305,455 0,385" fill="var(--steel)"/>
      <polygon points="14,0 290,0 290,410 14,362" fill="var(--charcoal)"/>
      <polygon points="178,410 290,338 290,410" fill="var(--rose)"/>
    </svg>
    <svg class="panel-art" viewBox="0 0 305 645">
      <defs>
        <linearGradient id="gymPhoto" x1="0" y1="0" x2="0" y2="1">
          <stop offset="0" stop-color="#e9ecef"/>
          <stop offset=".55" stop-color="#9aa2aa"/>
          <stop offset="1" stop-color="#5c5f63"/>
        </linearGradient>
      </defs>
      <polygon points="0,375 305,440 305,645 0,645" fill="url(#gymPhoto)" role="img" aria-label="Photo: trainer coaching a client doing push-ups on an orange agility ladder in a bright studio"/>
    </svg>
    <h2 class="about-title">About Velvet</h2>
    <span class="about-title-rule"></span>
    <div class="about-copy">
      <p>Velvet Stride is a revolutionary fitness studio focused on group and personal training. Our unique combination of effective training in an inspiring atmosphere is ideal for those looking for results.</p>
      <p>At Velvet Stride, you will experience the best instructors trained to deliver first class services and personal attention. We cater to YOUR goals, needs, and level of fitness.</p>
      <p>During each workout, you will engage in resistance training to increase your metabolism, work core muscles to strengthen and tone the mid-section, utilize your own body weight to challenge and improve balance and flexibility and increase your heart rate to burn maximum calories and fat.</p>
      <p>Beyond providing a unique workout method, our trainers' inspirational coaching approach will leave you feeling strong, confidant, and Velvet.</p>
    </div>
  </section>

  <section class="panel panel--contact">
    <svg class="panel-art" viewBox="0 0 305 645">
      <defs>
        <linearGradient id="bandPhoto" x1="0" y1="0" x2="0" y2="1">
          <stop offset="0" stop-color="#f4f4f4"/>
          <stop offset="1" stop-color="#cfcfd2"/>
        </linearGradient>
      </defs>
      <rect x="40" y="0" width="210" height="400" fill="url(#bandPhoto)" role="img" aria-label="Photo: woman in black sportswear training with a resistance band"/>
      <polygon points="0,440 305,316 305,330 0,456" fill="var(--rose)"/>
      <polygon points="0,456 305,330 305,645 0,645" fill="var(--charcoal)"/>
    </svg>
    <div class="brand brand--contact">
      <span class="brand-dot"></span>
      <span class="brand-name">Velvet Stride</span>
      <span class="brand-place">Crescent Bay</span>
    </div>
    <div class="social-row" aria-hidden="true"><span></span><span></span><span></span><span></span><span></span><span></span></div>
    <h3 class="contact-title">GET IN TOUCH</h3>
    <ul class="contact-list">
      <li>
        <svg width="13" height="13" viewBox="0 0 13 13"><circle cx="6.5" cy="6.5" r="5.8" fill="none" stroke="#fff" stroke-width="1.2"/><path d="M6.5 3a2 2 0 0 1 2 2c0 1.5-2 4-2 4s-2-2.5-2-4a2 2 0 0 1 2-2z" fill="#fff"/></svg>
        <span>418 Crescent Ave<br>Crescent Bay, CA 90412</span>
      </li>
      <li class="contact-phone">
        <svg width="13" height="13" viewBox="0 0 13 13"><circle cx="6.5" cy="6.5" r="5.8" fill="none" stroke="#fff" stroke-width="1.2"/><path d="M4.3 3.6l1.2 1.3-.6.9c.4.9 1.1 1.6 2 2l.9-.6 1.3 1.2-.7 1c-2.3-.2-4.3-2.2-4.5-4.5z" fill="#fff"/></svg>
        <span>(310) 555-0148</span>
      </li>
      <li class="contact-mail">
        <svg width="13" height="13" viewBox="0 0 13 13"><circle cx="6.5" cy="6.5" r="5.8" fill="none" stroke="#fff" stroke-width="1.2"/><rect x="3.6" y="4.6" width="5.8" height="3.8" fill="none" stroke="#fff" stroke-width=".9"/><path d="M3.6 4.6l2.9 2.2 2.9-2.2" fill="none" stroke="#fff" stroke-width=".9"/></svg>
        <span>info@velvetstride.com</span>
      </li>
      <li class="contact-web">
        <svg width="13" height="13" viewBox="0 0 13 13"><circle cx="6.5" cy="6.5" r="5.8" fill="none" stroke="#fff" stroke-width="1.2"/><circle cx="6.5" cy="6.5" r="3" fill="none" stroke="#fff" stroke-width=".9"/><path d="M3.5 6.5h6M6.5 3.5v6" stroke="#fff" stroke-width=".8"/></svg>
        <span>www.<b>velvetstride</b>.com</span>
      </li>
    </ul>
  </section>

  <section class="panel panel--cover">
    <svg class="panel-art" viewBox="0 0 304 645">
      <defs>
        <linearGradient id="sunsetPhoto" x1="0" y1="0" x2="0" y2="1">
          <stop offset="0" stop-color="#3b3a3c"/>
          <stop offset=".45" stop-color="#8c7a62"/>
          <stop offset=".8" stop-color="#e0b070"/>
          <stop offset="1" stop-color="#5a4a3e"/>
        </linearGradient>
      </defs>
      <rect x="0" y="0" width="304" height="360" fill="url(#sunsetPhoto)" role="img" aria-label="Photo: athlete holding an arm-balance pose on a rooftop at sunset above a city skyline"/>
      <polygon points="0,318 304,362 304,378 0,334" fill="var(--rose)"/>
      <polygon points="0,334 304,378 304,645 0,645" fill="var(--charcoal)"/>
    </svg>
    <div class="brand brand--cover">
      <span class="brand-dot"></span>
      <span class="brand-name">Velvet Stride</span>
      <span class="brand-place">Crescent Bay</span>
    </div>
    <h1 class="cover-headline">
      <span class="cover-kicker">Experience the</span>
      <span class="cover-title">Velvet Stride</span>
      <span class="cover-method">Track Method</span>
      <span class="cover-author">By Dana Whitfield</span>
    </h1>
    <div class="cover-spine"><span>www.<b>velvetstride</b>.com</span></div>
  </section>

</main>
</body>
</html>
```